Im open to ideas.. I was thinking on my business cards aswell as my logo. a place for my name. email. phone number and abn..

ive attched a file with my business logo. which i dont love the colours.. i was think a dark background with charcoal letters so something along those colour schumes but im open to ideas..

Business

BRL Constructions

```html
<!DOCTYPE html>
<html lang="en">
<head>
<meta charset="utf-8">
<title>BRL Constructions — Business Card</title>
<link href="https://fonts.googleapis.com/css2?family=Arimo:wght@400;700&family=Tinos&display=swap" rel="stylesheet">
<style>
  :root {
    --backdrop: #2b2b2b;
    --card: #f4f4f4;
    --card-shade: #e6e6e6;
    --accent: #d42a1c;
    --accent-band: #c0161b;
    --charcoal: #262626;
    --ink: #444444;
    --white: #ffffff;
  }
  html, body {
    margin: 0;
    padding: 0;
    width: 1200px;
    height: 997px;
    overflow: hidden;
    background: var(--backdrop);
  }
  .card {
    position: absolute;
    left: 180px;
    top: 258px;
    width: 840px;
    height: 480px;
    background: linear-gradient(160deg, var(--white) 0%, var(--card) 55%, var(--card-shade) 100%);
    overflow: hidden;
    font-family: "Arimo", Arial, sans-serif;
  }
  .holder {
    position: absolute;
    left: 64px;
    top: 60px;
  }
  .holder-name {
    margin: 0;
    font-family: "Tinos", "Times New Roman", serif;
    font-weight: 400;
    font-size: 34px;
    color: var(--accent);
    letter-spacing: 0.5px;
  }
  .holder-role {
    margin: 4px 0 0;
    font-size: 19px;
    color: var(--ink);
  }
  .brand {
    position: absolute;
    right: 52px;
    top: 238px;
    display: flex;
    align-items: center;
    gap: 12px;
  }
  .brand-mark {
    width: 22px;
    height: 22px;
    background: var(--accent);
  }
  .brand-name {
    font-size: 38px;
    font-weight: 700;
    color: var(--charcoal);
    letter-spacing: 1px;
  }
  .contact-tab {
    position: absolute;
    left: 0;
    top: 322px;
    width: 42px;
    height: 92px;
    background: var(--charcoal);
    border-radius: 0 10px 10px 0;
    display: flex;
    flex-direction: column;
    justify-content: space-evenly;
    align-items: center;
  }
  .contact-tab svg { width: 18px; height: 18px; }
  .contact-list {
    position: absolute;
    left: 62px;
    top: 330px;
    margin: 0;
    padding: 0;
    list-style: none;
    font-size: 19px;
    color: var(--ink);
    line-height: 40px;
  }
  .accent-band {
    position: absolute;
    left: 0;
    right: 0;
    bottom: 0;
    height: 16px;
    background: var(--accent-band);
  }
  .web-bar {
    position: absolute;
    right: 0;
    bottom: 0;
    width: 300px;
    height: 44px;
    background: var(--charcoal);
    border-top-left-radius: 30px;
    color: var(--white);
    font-size: 17px;
    display: flex;
    align-items: center;
    justify-content: center;
    letter-spacing: 0.3px;
  }
</style>
</head>
<body>
  <section class="card">
    <div class="holder">
      <h1 class="holder-name">Daniel R Moreno</h1>
      <p class="holder-role">Managing Partner</p>
    </div>

    <div class="brand">
      <span class="brand-mark"></span>
      <span class="brand-name">BRL Constructions</span>
    </div>

    <div class="contact-tab">
      <svg viewBox="0 0 24 24" aria-label="Phone">
        <path fill="#d42a1c" d="M6.6 10.8a15.2 15.2 0 0 0 6.6 6.6l2.2-2.2a1 1 0 0 1 1-.25 11.4 11.4 0 0 0 3.6.57 1 1 0 0 1 1 1V20a1 1 0 0 1-1 1A17 17 0 0 1 3 4a1 1 0 0 1 1-1h3.5a1 1 0 0 1 1 1c0 1.25.2 2.45.57 3.57a1 1 0 0 1-.25 1z"/>
      </svg>
      <svg viewBox="0 0 24 24" aria-label="Email">
        <rect x="2" y="5" width="20" height="14" rx="1.5" fill="#d42a1c"/>
        <path d="M3 6.5l9 6.5 9-6.5" fill="none" stroke="#262626" stroke-width="1.6"/>
      </svg>
    </div>

    <ul class="contact-list">
      <li class="contact-phone">+1 (555) 014-2286</li>
      <li class="contact-email">daniel@brlconstructions.com</li>
    </ul>

    <div class="accent-band"></div>
    <div class="web-bar">www.brlconstructions.com</div>
  </section>
</body>
</html>
```